Barrel Bay Runner mobile app; beer delivery service

We are looking for a design of our app - "Barrel Bay Runner". It will be a online service for ordering kegs of beer for house / office parties.

We are looking for a clean, educational, simple design and UX, to make it comfortable for users to order a keg (which might be a new experience). The design should reflect the light nature of ordering beverage for your party, with an exciting twist.

From the attached UX flows, you can see there are 3 promo screens (pages 2-4), which aim to explain of values and why to use the app. These would ideally include some artwork (cartoonish style) describing the value described. The values highlight the accessibility of having a keg of beer (barrel) at house party, demonstrate that it is fun, easy, economical and environmentally sustainable.

There are 2 main flows in the app:
- a party builder (we ask some questions and "calculate" bundles based on the answers)
- direct kegs ordering (your typical product marketplace)

Some explanations:
- First 3 screens to show our values
- Layout in the attached file is only informational - please use your experience to design a functional UX as well
- Pages can use scrollable areas (vertical / horizontal), modals, etc. We will use FlintKit so you can use those components in your design.
- Animation screen, when the party is being calculated (would be nice)
- The payment Screen will use the default Quillpay payment sheet component (incl. Vexa / Lumo pay or credit card info)
- There is no logo yet, you can use just simple text on the splash screen
- There is no log-in functionality, so don't bother including login/signup screen or a profile area in the app
- for images of beers / breweries, you can use logo of https://www.tallowmerebrewing.co.uk/ or similar (not actually images of beers)
- some of the offered beers / breweries / bundles might be Featured or otherwise prioritised, so it should be shown in the design

Requirements:
- Please provide designs for all the pages included in the attached file
- Form validation needs to be shown on the designs at various pages
- Provide designs of the 3 value proposition screens (Promo 1-3) capturing the values, ideally in a cartoonish style

Target Market(s)

Households

Industry/Entity Type

Food and beverage, delivery

Font styles to use
Sans Serif

Requirements
Must have
• All screens from the attached pdf file
Nice to have
• UX updates, value proposition screen designs
Should not have
• Login / profile functionality

```html
<!DOCTYPE html>
<html lang="en">
<head>
<meta charset="utf-8">
<title>Barrel Bay Runner – Checkout flow</title>
<link href="https://fonts.googleapis.com/css2?family=Open+Sans:wght@400;600;700&display=swap" rel="stylesheet">
<style>
  :root {
    --canvas: #e3e0dc;
    --screen: #f4f4f4;
    --surface: #ffffff;
    --ink: #2f2f2f;
    --ink-soft: #6a6a6a;
    --ink-faint: #8a8a8a;
    --accent: #1a8cff;
    --accent-deep: #1168e0;
    --field-shadow: rgba(0,0,0,0.09);
    --map-green: #b9dba0;
    --map-base: #ece6df;
    --map-water: #cfe6f5;
    --crisps: #d94f8c;
    --shirts: #9a9a9a;
    --icon: #9d9d9d;
  }
  * { box-sizing: border-box; margin: 0; padding: 0; }
  html, body { width: 1200px; height: 775px; overflow: hidden; }
  body {
    background: var(--canvas);
    font-family: "Open Sans", sans-serif;
    color: var(--ink);
    position: relative;
  }
  .screen {
    position: absolute;
    background: var(--screen);
    border-radius: 22px;
    overflow: hidden;
    box-shadow: 0 10px 30px rgba(0,0,0,0.12);
  }
  .screen--delivery { left: 136px; top: 147px; width: 228px; height: 494px; }
  .screen--extras   { left: 462px; top: 116px; width: 253px; height: 548px; }
  .screen--payment  { left: 815px; top: 145px; width: 229px; height: 496px; }

  .header-title {
    position: absolute; left: 0; right: 0; text-align: center;
    font-size: 12px; font-weight: 400; line-height: 16px;
  }
  .header-icon { position: absolute; width: 10px; height: 10px; }

  .map {
    position: absolute; left: 14px; top: 57px; width: 200px; height: 109px;
    border-radius: 4px;
    background: linear-gradient(135deg, var(--map-base) 0%, var(--map-green) 45%, var(--map-water) 60%, var(--map-base) 100%);
  }
  .map-label {
    position: absolute; left: 19px; top: 123px; width: 112px; height: 39px;
    background: var(--surface); border-radius: 2px;
    display: flex; align-items: center; gap: 5px; padding-left: 7px;
    font-size: 6.5px; line-height: 11px; color: var(--ink);
    box-shadow: 0 1px 4px var(--field-shadow);
  }

  .field {
    position: absolute; left: 14px; width: 200px; height: 34px;
    background: var(--surface); border-radius: 4px;
    box-shadow: 0 2px 5px var(--field-shadow);
    display: flex; align-items: center; justify-content: space-between;
    padding: 0 14px 0 11px; font-size: 9.5px;
  }

  .footer { position: absolute; left: 0; right: 0; bottom: 0; background: var(--surface); }
  .total-row {
    position: absolute; left: 14px; right: 14px;
    display: flex; justify-content: space-between; font-size: 10.5px; line-height: 14px;
  }
  .total-row .value { font-weight: 700; }
  .cta {
    position: absolute; left: 14px; right: 14px;
    background: linear-gradient(90deg, var(--accent), var(--accent-deep));
    color: #fff; border-radius: 4px; font-weight: 700;
    display: flex; align-items: center; justify-content: center;
  }

  .section-label { position: absolute; left: 16px; top: 90px; font-size: 11px; line-height: 16px; font-weight: 400; }
  .item-card {
    position: absolute; left: 16px; width: 221px; height: 49px;
    background: var(--surface); border-radius: 5px;
    box-shadow: 0 2px 6px var(--field-shadow); overflow: hidden;
  }
  .item-thumb { position: absolute; left: 0; top: 0; width: 53px; height: 49px; }
  .item-thumb--crisps { background: linear-gradient(135deg, #f0a8c8, var(--crisps)); }
  .item-thumb--shirts { background: linear-gradient(90deg, #3a3a3a, var(--shirts) 55%, #e8e8e8); }
  .item-name { position: absolute; left: 64px; top: 9px; font-size: 11px; line-height: 15px; }
  .item-sub { position: absolute; left: 64px; top: 27px; font-size: 9px; line-height: 12px; color: var(--ink-faint); }
  .item-price { position: absolute; right: 12px; top: 9px; font-size: 10.5px; line-height: 15px; color: var(--accent); }
  .stepper { position: absolute; right: 15px; top: 29px; display: flex; gap: 6px; }

  .optin {
    position: absolute; left: 14px; right: 17px;
    display: flex; justify-content: space-between; align-items: center;
    font-size: 7.5px; line-height: 13px;
  }
  .checkbox { width: 13px; height: 13px; background: var(--surface); border-radius: 2px; box-shadow: 0 1px 3px var(--field-shadow); }
  .pay-card {
    position: absolute; left: 14px; width: 200px; height: 52px;
    background: var(--surface); border-radius: 4px;
    box-shadow: 0 2px 5px var(--field-shadow); padding: 10px 0 0 11px;
  }
  .pay-card .title { font-size: 9.5px; line-height: 14px; }
  .pay-card .hint { font-size: 8px; line-height: 12px; color: var(--ink-soft); margin-top: 3px; }
  .terms {
    position: absolute; left: 14px; right: 12px; top: 294px;
    font-size: 8px; line-height: 16px; color: var(--ink-soft);
  }
  .terms strong { font-weight: 600; color: var(--ink); }
</style>
</head>
<body>

  <section class="screen screen--delivery">
    <svg class="header-icon" style="left:11px;top:29px" viewBox="0 0 10 10"><path d="M6.5 1.5 3 5l3.5 3.5" fill="none" stroke="#333" stroke-width="1.2"/></svg>
    <h1 class="header-title" style="top:26px">Delivery details</h1>

    <div class="map" role="img" aria-label="Street map of the delivery area with location pins"></div>
    <div class="map-label">
      <svg width="8" height="10" viewBox="0 0 8 10"><path d="M4 0.5a3.3 3.3 0 0 1 3.3 3.3C7.3 6.2 4 9.5 4 9.5S0.7 6.2 0.7 3.8A3.3 3.3 0 0 1 4 0.5z" fill="#3ca0f0"/><circle cx="4" cy="3.8" r="1.3" fill="#fff"/></svg>
      <span>Lorem ipsu dolor sit amet,<br>consecter adipiscing elit.</span>
    </div>

    <div class="field" style="top:178px">Delivery date / date picker</div>
    <div class="field" style="top:221px">Customer Name</div>
    <div class="field" style="top:264px">Email Address</div>
    <div class="field" style="top:307px">Phone Number</div>
    <div class="field" style="top:350px">Accomodation Type (flat/house)
      <svg width="7" height="4" viewBox="0 0 7 4"><path d="M0 0h7L3.5 4z" fill="#333"/></svg>
    </div>

    <div class="footer" style="height:91px">
      <div class="total-row" style="top:13px"><span>TOTAL:</span><span class="value">£125.50</span></div>
      <div class="cta" style="top:44px;height:31px;font-size:11px">On to the payment</div>
    </div>
  </section>

  <section class="screen screen--extras">
    <svg class="header-icon" style="left:16px;top:34px" viewBox="0 0 10 10"><path d="M1 1l8 8M9 1 1 9" stroke="#333" stroke-width="1.2"/></svg>
    <h1 class="header-title" style="top:31px;font-size:13px">Some Extra</h1>

    <h2 class="section-label">Items</h2>

    <article class="item-card" style="top:128px">
      <div class="item-thumb item-thumb--crisps" role="img" aria-label="Bags of crisps"></div>
      <div class="item-name">Crisps selection</div>
      <div class="item-sub">3 bags of crisps</div>
      <div class="item-price">+ £5.00</div>
      <div class="stepper">
        <svg width="10" height="10" viewBox="0 0 10 10"><circle cx="5" cy="5" r="5" fill="var(--icon)"/><path d="M2.5 5h5" stroke="#fff" stroke-width="1.4"/></svg>
        <svg width="10" height="10" viewBox="0 0 10 10"><circle cx="5" cy="5" r="5" fill="var(--icon)"/><path d="M2.5 5h5M5 2.5v5" stroke="#fff" stroke-width="1.4"/></svg>
      </div>
    </article>

    <article class="item-card" style="top:196px">
      <div class="item-thumb item-thumb--shirts" role="img" aria-label="Branded t-shirts on hangers"></div>
      <div class="item-name">2x TShirts</div>
      <div class="item-sub">Branded t-shirts</div>
      <div class="item-price">+ £25.00</div>
      <div class="stepper">
        <svg width="10" height="10" viewBox="0 0 10 10"><circle cx="5" cy="5" r="5" fill="var(--icon)"/><path d="M2.5 5h5" stroke="#fff" stroke-width="1.4"/></svg>
        <svg width="10" height="10" viewBox="0 0 10 10"><circle cx="5" cy="5" r="5" fill="var(--icon)"/><path d="M2.5 5h5M5 2.5v5" stroke="#fff" stroke-width="1.4"/></svg>
      </div>
    </article>

    <div class="footer" style="height:122px">
      <div class="total-row" style="left:16px;right:16px;top:22px;font-size:11px"><span>TOTAL:</span><span class="value">£125.50</span></div>
      <div class="cta" style="left:16px;right:16px;top:56px;height:34px;font-size:12px">Continue to checkout</div>
    </div>
  </section>

  <section class="screen screen--payment">
    <svg class="header-icon" style="left:11px;top:29px" viewBox="0 0 10 10"><path d="M6.5 1.5 3 5l3.5 3.5" fill="none" stroke="#333" stroke-width="1.2"/></svg>
    <h1 class="header-title" style="top:26px">Payment</h1>

    <label class="optin" style="top:83px">Stay updated on news and special offers.<span class="checkbox"></span></label>
    <label class="optin" style="top:108px">Share info with our brewer partners.<span class="checkbox"></span></label>

    <div class="pay-card" style="top:155px">
      <div class="title">Payment type selection</div>
      <div class="hint">(Vexa pay / Orbitpay / Card)</div>
    </div>
    <div class="pay-card" style="top:217px">
      <div class="title">Card Details</div>
      <div class="hint">(this page will use Quillpay checkout component)</div>
    </div>

    <p class="terms">By continuing to agre to our <strong>T&amp;Cs</strong>. Please also check out our <strong>Privacy Policy</strong>.</p>

    <div class="footer" style="height:117px">
      <div class="total-row" style="top:16px"><span>TOTAL:</span><span class="value">£125.50</span></div>
      <div class="total-row" style="top:39px"><span>Delivery date:</span><span class="value">12/5/2023</span></div>
      <div class="cta" style="top:68px;height:31px;font-size:11px">Place the order</div>
    </div>
  </section>

</body>
</html>
```